Construction company focused on concrete and shed construction.

We need to update our current business card for ridgeforgebuilds.com.au we would like an eye catching design with blue, grey and white incorporating our current logo.
Our company started off in concreting and due to varying factors we have expanded to include shed construction as well.
This has led to our current Logo looking a little out of place and somehow need to use the card to bring in the shed construction side of the business while not having to change current concrete look "KESTRO" logo as we already have this incorporated into our company clothing and are not willing to change this yet.
Photo image attached for inspiration/ visual reference of type of work, not to be used on final design.
Please no cheesy designs of men in hard hats and tools
Final design should demonstrate a modern and service focused company.

Target Market(s)

Farmers, Business owners, Developers, Architects, Commercial project delivery

Industry/Entity Type

Construction Company

Contact Information for Business Card

Kestro Constructions.
7b Harlow st
North Castleford Qld
03 62918873

Font styles to use
Other font styles liked:
• see font in logo

Colors
3176b5
b2b2b2

Requirements
Must have
• Easy to read font,
• good contrast between back ground and writing
Nice to have
• Modern and corporate look with a fun but professional image.
Should not have
• Comic images or shadow images of tools/ people.

```html
<!DOCTYPE html>
<html lang="en">
<head>
<meta charset="utf-8">
<title>Kestro Constructions – Business Card</title>
<link href="https://fonts.googleapis.com/css2?family=Lato:wght@400;700&display=swap" rel="stylesheet">
<style>
  :root {
    --backdrop: #535353;
    --card-light: #e8e8e8;
    --brand-blue: #1d5b9c;
    --brand-blue-bright: #2f74b5;
    --brand-blue-deep: #17599a;
    --text-grey: #404040;
    --rule-grey: #4b5e72;
    --white: #ffffff;
  }
  * { margin: 0; padding: 0; box-sizing: border-box; }
  html, body { width: 1200px; height: 900px; overflow: hidden; }
  body {
    background: var(--backdrop);
    font-family: "Lato", Arial, sans-serif;
    position: relative;
  }
  .card {
    position: absolute;
    top: 170px;
    width: 342px;
    height: 561px;
    border-radius: 18px;
    box-shadow: 3px 4px 6px rgba(0,0,0,0.45);
    overflow: hidden;
  }
  .card-front { left: 262px; background: var(--card-light); text-align: center; }
  .card-back {
    left: 633px;
    background: radial-gradient(circle at 50% 50%, var(--brand-blue-bright) 0%, var(--brand-blue-deep) 75%);
  }
  .brand-mark {
    position: absolute;
    left: 50%;
    transform: translateX(-50%);
    display: flex;
    align-items: center;
    justify-content: center;
    border-radius: 50%;
  }
  .card-front .brand-mark {
    top: 80px;
    width: 150px;
    height: 150px;
    border: 3px solid var(--brand-blue);
  }
  .card-back .brand-mark {
    top: 192px;
    width: 176px;
    height: 176px;
    background: var(--white);
  }
  .brand-name {
    font-weight: 700;
    color: var(--brand-blue);
    font-size: 26px;
    letter-spacing: 1px;
  }
  .person-name {
    position: absolute; left: 0; right: 0; top: 294px;
    font-size: 21px; font-weight: 400; color: var(--brand-blue);
    letter-spacing: 0.3px;
  }
  .person-role {
    position: absolute; left: 0; right: 0; top: 319px;
    font-size: 16px; color: var(--text-grey);
  }
  .divider {
    position: absolute; left: 90px; width: 162px; height: 32px;
  }
  .divider-phone { top: 352px; }
  .divider-pin { top: 420px; }
  .phone-number {
    position: absolute; left: 0; right: 0; top: 389px;
    font-size: 17px; color: var(--text-grey); letter-spacing: 0.5px;
  }
  .company-name {
    position: absolute; left: 0; right: 0; top: 459px;
    font-size: 16px; font-weight: 400; color: var(--brand-blue);
    letter-spacing: 0.2px;
  }
  .address {
    position: absolute; left: 0; right: 0; top: 480px;
    font-size: 16px; line-height: 20px; color: var(--text-grey);
  }
</style>
</head>
<body>
  <section class="card card-front">
    <div class="brand-mark"><span class="brand-name">KESTRO</span></div>
    <h1 class="person-name">MARCUS REID</h1>
    <p class="person-role">Managing Director</p>

    <svg class="divider divider-phone" viewBox="0 0 162 32" aria-hidden="true">
      <line x1="0" y1="16" x2="60" y2="16" stroke="var(--rule-grey)" stroke-width="1"/>
      <line x1="102" y1="16" x2="162" y2="16" stroke="var(--rule-grey)" stroke-width="1"/>
      <circle cx="81" cy="16" r="16" fill="var(--brand-blue)"/>
      <path d="M75 9c1-1 2-1 3 0l2 3c.5 1 .3 1.7-.5 2.3l-1 .8c.8 2 2.3 3.5 4.3 4.3l.8-1c.6-.8 1.3-1 2.3-.5l3 2c1 1 1 2 0 3l-1.2 1.2c-1.3 1.3-4 .8-7-1.7-3-2.5-5-5.8-5.4-7.8-.3-1.4 0-2.6.7-3.3z" fill="var(--white)"/>
    </svg>
    <p class="phone-number">03 62918873</p>

    <svg class="divider divider-pin" viewBox="0 0 162 32" aria-hidden="true">
      <line x1="0" y1="16" x2="60" y2="16" stroke="var(--rule-grey)" stroke-width="1"/>
      <line x1="102" y1="16" x2="162" y2="16" stroke="var(--rule-grey)" stroke-width="1"/>
      <circle cx="81" cy="16" r="16" fill="var(--brand-blue)"/>
      <path d="M81 7a6 6 0 0 1 6 6c0 4.5-6 11-6 11s-6-6.5-6-11a6 6 0 0 1 6-6z" fill="var(--white)"/>
      <circle cx="81" cy="13" r="2.3" fill="var(--brand-blue)"/>
    </svg>
    <p class="company-name">KESTRO CONSTRUCTIONS</p>
    <p class="address">7b Harlow st<br>North Castleford Qld</p>
  </section>

  <section class="card card-back" role="img" aria-label="Blue sunburst ray pattern radiating from the centre">
    <div class="brand-mark"><span class="brand-name">KESTRO</span></div>
  </section>
</body>
</html>
```